11 x 11 Flyer Design for Social Media - Reverse Mortgages

62 or older?

A Reverse Mortgage
could be
Your Road to Financial Freedom

* No Monthly Payments
* No Income Requirements
* No Credit Score Requirements
* No Loss of Ownership

Receive cash by lump sum, monthly installments or a line of credit!!

Call us today for a Free Consultation!!
(800) 647-2915

Harborline Financial Services, Inc.
NMLS #517830
www.harborlinefunds.example

```html
<!DOCTYPE html>
<html lang="en">
<head>
<meta charset="UTF-8">
<title>Reverse Mortgage Flyer – Harborline Financial Services</title>
<link href="https://fonts.googleapis.com/css2?family=Montserrat:wght@400;500;700;800&display=swap" rel="stylesheet">
<style>
  :root {
    --blue: #0b5aa6;
    --blue-deep: #0a4e93;
    --gold: #a89a2c;
    --gold-light: #e6d24a;
    --ink: #1c1c1c;
    --grey: #3a3a3a;
    --page: #eef0f2;
    --white: #ffffff;
  }
  * { box-sizing: border-box; margin: 0; padding: 0; }
  html, body { width: 857px; height: 1200px; overflow: hidden; }
  body {
    background: var(--page);
    font-family: "Montserrat", Arial, sans-serif;
    color: var(--ink);
    position: relative;
  }
  .flyer {
    position: absolute;
    left: 28px; top: 200px;
    width: 800px; height: 800px;
    background: var(--white);
    box-shadow: 0 4px 14px rgba(0,0,0,.12);
    overflow: hidden;
  }
  .flyer > * { position: absolute; }

  .brand {
    left: 48px; top: 70px;
    display: flex; align-items: center; gap: 10px;
    font-weight: 700; font-size: 17px; line-height: 1.15;
    color: var(--blue);
  }
  .brand-dot {
    width: 34px; height: 34px; border-radius: 50%;
    background: var(--gold);
    flex: none;
  }

  .hero-photo { left: 0; top: 0; width: 800px; height: 500px; }

  .headline-age { left: 33px; top: 178px; color: var(--blue); font-weight: 800; line-height: 1; }
  .headline-age .num { font-size: 52px; }
  .headline-age .or { font-size: 40px; font-weight: 500; margin-left: 8px; }
  .headline-age .older { display: block; font-size: 56px; margin-top: 6px; letter-spacing: .5px; }

  .rule { left: 33px; top: 306px; width: 230px; height: 2px; background: #7a7a7a; }
  .rule::before { content: ""; position: absolute; left: 0; top: -1px; width: 34px; height: 4px; background: var(--gold-light); }

  .headline-product {
    left: 32px; top: 318px;
    color: var(--gold); font-weight: 800;
    font-size: 44px; line-height: 1; letter-spacing: .5px;
  }
  .tagline { left: 33px; top: 418px; line-height: 1.02; }
  .tagline .lead { display: block; font-size: 25px; font-weight: 400; color: var(--ink); letter-spacing: .3px; }
  .tagline .strong { display: block; font-size: 30px; font-weight: 700; color: var(--ink); }

  .benefits-band { left: 0; top: 500px; width: 800px; height: 170px; }

  .benefit {
    width: 150px; text-align: center;
    color: var(--white); font-weight: 700; font-size: 11.5px; line-height: 1.25;
  }
  .benefit svg { display: block; margin: 0 auto 6px; }

  .offer-pill {
    left: 34px; top: 650px; width: 731px; height: 48px;
    background: var(--gold); border-radius: 10px;
    border: 2px solid var(--white);
    box-shadow: 0 0 0 1px var(--gold);
    color: var(--white); font-weight: 700; font-size: 18px;
    display: flex; align-items: center; justify-content: center;
    letter-spacing: .2px;
  }

  .call { left: 46px; top: 721px; }
  .call .prompt { font-weight: 700; font-size: 17px; color: var(--ink); }
  .call .phone { display: flex; align-items: center; gap: 10px; margin-top: 2px; font-weight: 700; font-size: 34px; color: var(--grey); }

  .company { left: 456px; top: 721px; font-size: 17px; line-height: 1.12; color: var(--grey); }
  .company .web { display: flex; align-items: center; gap: 5px; font-weight: 700; font-size: 18px; color: var(--ink); }
</style>
</head>
<body>
  <main class="flyer">
    <svg class="hero-photo" viewBox="0 0 800 500" aria-hidden="false">
      <defs>
        <clipPath id="photoCircle"><circle cx="570" cy="190" r="278"/></clipPath>
        <linearGradient id="beachTones" x1="0" y1="0" x2="0" y2="1">
          <stop offset="0" stop-color="#b9c6cf"/>
          <stop offset=".4" stop-color="#d9dfe2"/>
          <stop offset=".7" stop-color="#c8b8a4"/>
          <stop offset="1" stop-color="#d8d2c8"/>
        </linearGradient>
      </defs>
      <path d="M570 190 m-284 0 a284 284 0 1 0 568 0" fill="none" stroke="var(--gold)" stroke-width="14" transform="rotate(-20 570 190)"/>
      <g role="img" aria-label="Photo of a smiling senior couple dressed in white, embracing on a beach">
        <rect x="280" y="-100" width="600" height="600" fill="url(#beachTones)" clip-path="url(#photoCircle)"/>
      </g>
      <circle cx="570" cy="190" r="279" fill="none" stroke="var(--white)" stroke-width="2"/>
    </svg>

    <div class="brand">
      <span class="brand-dot"></span>
      <span>Harborline<br>Financial Services, Inc.</span>
    </div>

    <h1 class="headline-age"><span class="num">62</span><span class="or">OR</span><span class="older">OLDER?</span></h1>
    <div class="rule"></div>
    <h2 class="headline-product">A REVERSE<br>MORTGAGE</h2>
    <p class="tagline"><span class="lead">Could be Your Road to</span><span class="strong">Financial Freedom</span></p>

    <svg class="benefits-band" viewBox="0 0 800 170">
      <path d="M0 85 C200 20 600 20 800 85 L800 164 L0 164 Z" fill="var(--blue)"/>
    </svg>

    <div class="benefit" style="left:26px;top:505px;">
      <svg width="96" height="96" viewBox="0 0 96 96">
        <circle cx="48" cy="48" r="46" fill="var(--blue)"/>
        <circle cx="48" cy="48" r="42" fill="var(--white)"/>
        <path d="M48 2 A46 46 0 0 1 94 48" fill="none" stroke="var(--gold)" stroke-width="4"/>
        <g fill="none" stroke="var(--ink)" stroke-width="2" stroke-linejoin="round" stroke-linecap="round">
          <rect x="42" y="28" width="24" height="14" rx="2" transform="rotate(-25 54 35)"/>
          <path d="M28 62 h8 l10 4 h14 l8 -6 M28 56 h10 l8 -3 h10"/>
        </g>
      </svg>
      No Monthly<br>Payments
    </div>

    <div class="benefit" style="left:220px;top:483px;">
      <svg width="96" height="96" viewBox="0 0 96 96">
        <circle cx="48" cy="48" r="46" fill="var(--blue)"/>
        <circle cx="48" cy="48" r="42" fill="var(--white)"/>
        <path d="M2 48 A46 46 0 0 1 94 48" fill="none" stroke="var(--gold)" stroke-width="4"/>
        <g fill="none" stroke="var(--ink)" stroke-width="2" stroke-linecap="round">
          <circle cx="45" cy="34" r="8"/>
          <path d="M32 64 v-10 a13 13 0 0 1 26 0 v10 z"/>
          <circle cx="58" cy="52" r="6"/>
        </g>
      </svg>
      No Income<br>Requirements
    </div>

    <div class="benefit" style="left:419px;top:483px;">
      <svg width="96" height="96" viewBox="0 0 96 96">
        <circle cx="48" cy="48" r="46" fill="var(--blue)"/>
        <circle cx="48" cy="48" r="42" fill="var(--white)"/>
        <path d="M2 48 A46 46 0 0 1 94 48" fill="none" stroke="var(--gold)" stroke-width="4"/>
        <g fill="none" stroke="var(--ink)" stroke-width="2" stroke-linecap="round">
          <rect x="32" y="26" width="28" height="40" rx="2"/>
          <path d="M37 36 h4 M44 36 h11 M37 44 h4 M44 44 h11 M37 52 h4 M44 52 h11 M37 60 h4 M44 60 h8"/>
        </g>
      </svg>
      No Credit Score<br>Requirements
    </div>

    <div class="benefit" style="left:612px;top:505px;">
      <svg width="96" height="96" viewBox="0 0 96 96">
        <circle cx="48" cy="48" r="46" fill="var(--blue)"/>
        <circle cx="48" cy="48" r="42" fill="var(--white)"/>
        <path d="M48 2 A46 46 0 0 1 94 48" fill="none" stroke="var(--gold)" stroke-width="4"/>
        <g fill="none" stroke="var(--ink)" stroke-width="2" stroke-linecap="round" stroke-linejoin="round">
          <rect x="32" y="56" width="8" height="10"/><rect x="43" y="50" width="8" height="16"/><rect x="54" y="44" width="8" height="22"/>
          <path d="M32 46 l12 -8 l8 4 l14 -12 M60 30 h6 v6"/>
          <circle cx="38" cy="32" r="6"/>
        </g>
      </svg>
      No Loss of<br>Ownership
    </div>

    <div class="offer-pill">Receive cash by lump sum, monthly installments or a line of credit!!</div>

    <div class="call">
      <p class="prompt">Call us today for a Free Consultation!!</p>
      <p class="phone">
        <svg width="26" height="26" viewBox="0 0 24 24" fill="none" stroke="var(--blue)" stroke-width="1.8" stroke-linejoin="round"><path d="M5 3 h4 l2 5 -2.5 1.5 a11 11 0 0 0 6 6 L16 13 l5 2 v4 a2 2 0 0 1 -2 2 A17 17 0 0 1 3 5 a2 2 0 0 1 2 -2z"/></svg>
        (800) 647-2915
      </p>
    </div>

    <div class="company">
      <p>Harborline Financial Services, Inc.</p>
      <p>NMLS #517830</p>
      <p class="web">
        <svg width="14" height="14" viewBox="0 0 24 24" fill="none" stroke="var(--blue)" stroke-width="2"><circle cx="12" cy="12" r="10"/><path d="M2 12 h20 M12 2 a15 15 0 0 1 0 20 a15 15 0 0 1 0 -20"/></svg>
        www.harborlinefunds.example
      </p>
    </div>
  </main>
</body>
</html>
```